A colorful, playful, nerdy, creative logo for a business analytics and marketing analytics company.

We need a logo and website design for a new company based in Florida called Brightfold Pattern Works Collective. We provide marketing, consumer and business insights through the use of market research, business analytics and marketing analytics. We are a collection of several individuals each with specific expertise and come together to provide the best possible insights about their consumers/guests/customers. We would like to see a design that uses colors that show a free spirit but deeply rooted in analytics " a super nerd " Along those steps, we would like to see either a playful, nerdy, creative logo or one that includes the full or partial name of the company. We have simplified our "brand" by saying when you initially start with us you may have several questions "?" through the process of learning about your consumers/brand ">" incredible solutions, strategies are developed "!" So something like a ?>! symbol would be interesting. Although the name of the company sounds very complex and very long to write, we would be interested in thoughtful ways of shorting the name or incorporating into the final logo design

Target Market(s)

Business or organizations that currently do not have an analytics/research function

Industry/Entity Type

Business

Contact Information for Business Card

Incorporate final logo and colors font. In the past, I have used a "wordle" website to show 10 common research terms scattered about .. showing them as strength or core competencies.

Logo Text

?>! or Brightfold Pattern Works Collective or BPW Collective

Coding

Coded - Design and coding required

Number of Pages Required

4 page

Font styles to use
Sans Serif
Decorative

Requirements
Must have
• The project must communicate analytics/scientific. It must we unique but not unique for the sack of being unique.
• It must either be a logo or a simple way to communicate the company name Brightfold Pattern Works Collective
Nice to have
• Again incorporating the symbols ?>! in that order. Showing confusion to gaining insights and then developing incredible solutions that are used to effect consumer behavior.
• Look to CPG ( consumer package goods) industry to input
Should not have
• I am pretty open to suggestions.

```html
<!DOCTYPE html>
<html lang="en">
<head>
<meta charset="utf-8">
<title>BPWC — Brightfold Pattern Works Collective</title>
<link href="https://fonts.googleapis.com/css2?family=Open+Sans:ital,wght@0,300;0,400;0,600;0,700;1,400;1,600&display=swap" rel="stylesheet">
<style>
:root{
  --teal:#33e0c3;
  --teal-deep:#22c9ad;
  --dark:#2c3038;
  --dark-2:#353a43;
  --ink:#2f3336;
  --text:#5d6166;
  --muted:#8d9196;
  --white:#ffffff;
  --line:#d9dcdf;
}
*{margin:0;padding:0;box-sizing:border-box}
html,body{width:1200px;height:4557px;overflow:hidden}
body{font-family:"Open Sans",Arial,sans-serif;color:var(--text);background:var(--white)}
section,header,footer{position:relative;width:1200px;overflow:hidden}
.abs{position:absolute}

/* header */
.site-header{height:182px;background:var(--dark)}
.brand{position:absolute;left:0;right:0;text-align:center}
.brand-name{font-weight:700;font-size:60px;letter-spacing:8px;color:var(--teal);line-height:1}
.brand-tagline{font-size:11px;color:var(--white);margin-top:4px;letter-spacing:.3px}
.site-header .brand{top:18px}
.main-nav{position:absolute;top:128px;left:0;right:0;display:flex;justify-content:center;gap:44px;align-items:center}
.main-nav a{color:var(--white);font-size:15px;text-decoration:none;text-transform:uppercase;position:relative}
.main-nav a.active{color:var(--teal)}
.main-nav a.active::after{content:"";position:absolute;left:50%;top:27px;margin-left:-6px;border:6px solid transparent;border-bottom:none;border-top:7px solid var(--teal)}

/* hero */
.hero{height:517px;background:linear-gradient(100deg,#6e7378 0%,#9ea3a6 30%,#c5c9cb 55%,#8f969b 78%,#5b6268 100%)}
.hero-photo{position:absolute;inset:0;background:linear-gradient(180deg,rgba(30,34,40,.15),rgba(30,34,40,.45))}
.hero-title{position:absolute;top:202px;left:0;right:0;text-align:center;color:var(--white);font-weight:700;font-size:42px;text-transform:uppercase;letter-spacing:-.5px}
.hero-sub{position:absolute;top:272px;left:0;right:0;text-align:center;color:var(--white);font-size:19px}
.btn-solid{position:absolute;top:311px;left:506px;width:188px;height:56px;background:var(--teal);color:var(--white);font-size:20px;text-transform:uppercase;display:flex;align-items:center;justify-content:center}
.hero-arrow{position:absolute;top:236px}

/* section titles */
.sec-title{position:absolute;left:0;right:0;text-align:center;font-weight:400;font-size:44px;text-transform:uppercase;color:var(--ink)}
.sec-sub{position:absolute;left:0;right:0;text-align:center;font-size:14px;color:var(--text)}

/* services */
.services{height:495px}
.service{position:absolute;top:178px;width:310px;text-align:center}
.service-icon{width:130px;height:100px;margin:0 auto;background:linear-gradient(135deg,#d9f8f2,#a7efe2);border-radius:6px}
.service h3{font-weight:400;font-size:18px;text-transform:uppercase;color:var(--ink);margin-top:40px}
.service p{font-size:13.5px;line-height:1.7;margin-top:14px;padding:0 20px}

/* welcome */
.welcome{height:468px;background:var(--teal)}
.welcome .sec-title{top:52px;color:var(--ink)}
.welcome .sec-sub{top:116px;color:var(--ink)}
.welcome-copy{position:absolute;top:150px;left:140px;width:920px;text-align:center;font-size:13.5px;line-height:1.7;color:#3e5853}
.welcome-copy p+p{margin-top:14px}
.btn-outline{position:absolute;width:186px;height:58px;border:1.5px solid var(--white);color:var(--white);font-size:20px;text-transform:uppercase;display:flex;align-items:center;justify-content:center}
.welcome .btn-outline{top:349px;left:507px}

/* expertise band */
.expertise{height:146px;background:var(--dark)}
.expertise-tab{position:absolute;left:0;top:0;width:334px;height:146px;background:var(--teal);border-radius:0 74px 0 0}
.expertise-tab span{position:absolute;left:76px;top:26px;font-size:42px;line-height:1.1;color:var(--white);text-transform:uppercase;font-weight:400}
.expertise-copy{position:absolute;left:368px;top:43px;width:690px;color:var(--white);font-size:15.5px;line-height:1.75}
.expertise-copy em{color:var(--teal);text-decoration:underline;font-style:italic}
.expertise-play{position:absolute;left:1058px;top:37px}

/* feature rows */
.feature{height:334px}
.feature.alt-teal{background:var(--teal)}
.feature.alt-dark{background:var(--dark)}
.feature-art{position:absolute;top:67px;width:200px;height:200px;border-radius:50%;background:radial-gradient(circle at 50% 45%,#ffffff 0,#f3f4f5 70%,#e3e5e7 100%);border:3px solid var(--line);box-shadow:0 4px 10px rgba(0,0,0,.18)}
.feature-text{position:absolute;top:104px;width:640px}
.feature-text h2{font-weight:400;font-size:34px;text-transform:uppercase;color:var(--ink)}
.feature-text p{font-size:14px;line-height:1.75;margin-top:16px;color:var(--text)}
.alt-teal .feature-text p{color:#3e7a70}
.alt-dark .feature-text h2{color:var(--white)}
.alt-dark .feature-text p{color:#8e949b}
.more{display:inline-flex;align-items:center;gap:14px;margin-top:12px;font-size:15px;font-style:italic;color:var(--teal);text-decoration:underline;text-transform:uppercase}
.alt-teal .more{color:var(--white)}

/* clients */
.clients{height:486px}
.clients .sec-title{top:54px}
.clients .sec-sub{top:118px}
.testimonial{position:absolute;top:190px;width:320px}
.quote-mark{font-weight:700;font-size:130px;line-height:.8;color:var(--teal);height:74px;overflow:hidden;letter-spacing:-6px}
.testimonial p{font-size:14px;line-height:1.75;margin-top:22px;color:var(--text)}
.client-name{margin-top:16px;text-align:right;font-size:15px;color:var(--teal);text-transform:uppercase;text-decoration:underline}
.client-name::before{content:"";display:inline-block;width:22px;height:2px;background:var(--teal);vertical-align:middle;margin-right:10px}

/* contact */
.contact{height:614px;background:var(--teal)}
.contact .sec-title{top:58px;color:var(--ink)}
.contact-sub{position:absolute;top:120px;left:0;right:0;text-align:center;font-size:19px;font-style:italic;font-weight:600;color:var(--white)}
.contact-item{position:absolute;top:172px;width:320px;text-align:center}
.contact-item .icon{width:82px;height:82px;border-radius:50%;background:var(--white);margin:0 auto;display:flex;align-items:center;justify-content:center}
.contact-item span{display:block;margin-top:26px;font-size:17px;color:var(--ink)}
.field{position:absolute;background:var(--white);font-size:14px;color:#777;padding:16px 14px}
.contact .btn-outline{top:492px;left:512px;width:176px;height:58px}

/* footer */
.site-footer{height:313px;background:var(--dark)}
.site-footer .brand{top:46px}
.social{position:absolute;top:148px;left:0;right:0;display:flex;justify-content:center;gap:8px}
.social i{width:48px;height:48px;border-radius:50%;border:2px solid #5f656c}
.social i.on{background:var(--teal);border-color:var(--teal)}
.footer-nav{position:absolute;top:216px;left:0;right:0;text-align:center;font-size:14px;color:var(--white)}
.footer-nav a{color:var(--white);text-decoration:none;padding:0 14px;border-right:1px solid var(--white)}
.footer-nav a:last-child{border-right:none}
.copyright{position:absolute;top:246px;left:0;right:0;text-align:center;font-size:13px;color:var(--white)}
</style>
</head>
<body>

<header class="site-header">
  <div class="brand">
    <div class="brand-name">BPWC</div>
    <div class="brand-tagline">Brightfold Pattern Works Collective</div>
  </div>
  <nav class="main-nav">
    <a href="#" class="active">Home</a>
    <a href="#">About Us</a>
    <a href="#">Process</a>
    <a href="#">Services</a>
    <a href="#">Expertise</a>
    <a href="#">Contact Us</a>
    <svg width="18" height="18" viewBox="0 0 18 18" aria-label="Search"><circle cx="7.5" cy="7.5" r="5.5" fill="none" stroke="#fff" stroke-width="2.2"/><line x1="11.5" y1="11.5" x2="16.5" y2="16.5" stroke="#fff" stroke-width="2.6" stroke-linecap="round"/></svg>
  </nav>
</header>

<section class="hero">
  <div class="hero-photo" role="img" aria-label="Photo of a person working on a laptop in a bright office"></div>
  <svg class="hero-arrow" style="left:30px" width="22" height="44" viewBox="0 0 22 44"><polyline points="20,2 2,22 20,42" fill="none" stroke="#d5d8da" stroke-width="2"/></svg>
  <svg class="hero-arrow" style="right:30px" width="22" height="44" viewBox="0 0 22 44"><polyline points="2,2 20,22 2,42" fill="none" stroke="#d5d8da" stroke-width="2"/></svg>
  <h1 class="hero-title">Brightfold Pattern Works Collective</h1>
  <p class="hero-sub">We provide marketing, consumer and business insights through the use of</p>
  <a class="btn-solid">Contact Us</a>
</section>

<section class="services">
  <h2 class="sec-title" style="top:56px">Our Best Services</h2>
  <p class="sec-sub" style="top:118px">We Provide You</p>
  <div class="service" style="left:112px">
    <div class="service-icon" role="img" aria-label="Line illustration of a chart with a magnifying glass"></div>
    <h3>Market Research</h3>
    <p>Lorem Ipsum is simply dummy text of the printing and typesetting industry. Lorem Ipsum has been the industry's standard dummy.</p>
  </div>
  <div class="service" style="left:447px">
    <div class="service-icon" role="img" aria-label="Line illustration of a presenter beside a chart board"></div>
    <h3>Business Analytics</h3>
    <p>Lorem Ipsum is simply dummy text of the printing and typesetting industry. Lorem Ipsum has been the industry's standard dummy.</p>
  </div>
  <div class="service" style="left:796px">
    <div class="service-icon" role="img" aria-label="Line illustration of a rising bar chart"></div>
    <h3>Marketing Analytics</h3>
    <p>Lorem Ipsum is simply dummy text of the printing and typesetting industry. Lorem Ipsum has been the industry's standard dummy.</p>
  </div>
</section>

<section class="welcome">
  <h2 class="sec-title">Welcome to BPWC</h2>
  <p class="sec-sub">Brightfold Pattern Works Collective</p>
  <div class="welcome-copy">
    <p>Lorem Ipsum is simply dummy text of the printing and typesetting industry. Lorem Ipsum has been the industry's standard dummy text ever since the 1500s, when an unknown printer took a galley of type. It has survived not only five centuries, but also the leap into.</p>
    <p>It has survived not only five centuries, but also the leap into electronic typesetting, remaining essentially unchanged. It was popularised in the 1960s with the release of Letraset sheets containing Lorem Ipsum passages, and more recently with desktop publishing software like it has survived not only five centuries, but also the leap into electronic typesetting, remaining essentially unchanged, a publishing software like it has survived not only five centuries, but also the leap into electronic typesetting, remaining essentially unchanged.</p>
  </div>
  <a class="btn-outline">Learn More</a>
</section>

<section class="expertise">
  <div class="expertise-tab"><span>Our<br>Expertise</span></div>
  <p class="expertise-copy">We are a collection of several individuals each with specific EXPERTISE and come together to provide the best possible insights about their: <em>CONSUMERS/GUESTS/CUSTOMERS</em></p>
  <svg class="expertise-play" width="72" height="72" viewBox="0 0 72 72" aria-label="Play"><circle cx="36" cy="36" r="33" fill="none" stroke="#33e0c3" stroke-width="3"/><polygon points="29,23 50,36 29,49" fill="#33e0c3"/></svg>
</section>

<section class="feature">
  <div class="feature-art" style="left:137px" role="img" aria-label="Sketch of a figure with a question mark above"></div>
  <div class="feature-text" style="left:450px">
    <h2>Several Questions ?</h2>
    <p>Lorem Ipsum is simply dummy text of the printing and typesetting industry. Lorem Ipsum has been the industry's standard dummy text ever since the printer took a galley.</p>
    <span class="more">Learn More <svg width="34" height="12" viewBox="0 0 34 12"><line x1="0" y1="6" x2="28" y2="6" stroke="currentColor" stroke-width="3"/><polygon points="26,0 34,6 26,12" fill="currentColor"/></svg></span>
  </div>
</section>

<section class="feature alt-teal">
  <div class="feature-text" style="left:80px">
    <h2>Process of Learning</h2>
    <p>Lorem Ipsum is simply dummy text of the printing and typesetting industry. Lorem Ipsum has been the industry's standard dummy text ever since the printer took a galley.</p>
    <span class="more">Learn More <svg width="34" height="12" viewBox="0 0 34 12"><line x1="0" y1="6" x2="28" y2="6" stroke="currentColor" stroke-width="3"/><polygon points="26,0 34,6 26,12" fill="currentColor"/></svg></span>
  </div>
  <div class="feature-art" style="left:842px" role="img" aria-label="Sketch of a thinking figure with gears above"></div>
</section>

<section class="feature">
  <div class="feature-art" style="left:137px" role="img" aria-label="Sketch of a figure with a light bulb above"></div>
  <div class="feature-text" style="left:450px">
    <h2>Incredible Solutions.</h2>
    <p>Lorem Ipsum is simply dummy text of the printing and typesetting industry. Lorem Ipsum has been the industry's standard dummy text ever since the printer took a galley.</p>
    <span class="more">Learn More <svg width="34" height="12" viewBox="0 0 34 12"><line x1="0" y1="6" x2="28" y2="6" stroke="currentColor" stroke-width="3"/><polygon points="26,0 34,6 26,12" fill="currentColor"/></svg></span>
  </div>
</section>

<section class="feature alt-dark">
  <div class="feature-text" style="left:80px">
    <h2>Strategies Are Developed.</h2>
    <p>Lorem Ipsum is simply dummy text of the printing and typesetting industry. Lorem Ipsum has been the industry's standard dummy text ever since the printer took a galley.</p>
    <span class="more">Learn More <svg width="34" height="12" viewBox="0 0 34 12"><line x1="0" y1="6" x2="28" y2="6" stroke="currentColor" stroke-width="3"/><polygon points="26,0 34,6 26,12" fill="currentColor"/></svg></span>
  </div>
  <div class="feature-art" style="left:842px" role="img" aria-label="Sketch of a figure with an exclamation mark above"></div>
</section>

<section class="clients">
  <h2 class="sec-title">Our Happy Clients</h2>
  <p class="sec-sub">Testimonials</p>
  <div class="testimonial" style="left:78px">
    <div class="quote-mark">&rdquo;</div>
    <p>" Lorem Ipsum is simply dummy text of the printing and typesetting industry. Lorem Ipsum has been the industry's standard dummy text ever since the printer took a galley ever since the printer ever since the printer took a galley. "</p>
    <div class="client-name">Client Name</div>
  </div>
  <div class="testimonial" style="left:434px">
    <div class="quote-mark">&rdquo;</div>
    <p>" Lorem Ipsum is simply dummy text of the printing and typesetting industry. Lorem Ipsum has been the industry's standard dummy text ever since the printer took a galley ever since the printer ever since the printer took a galley. "</p>
    <div class="client-name">Client Name</div>
  </div>
  <div class="testimonial" style="left:790px">
    <div class="quote-mark">&rdquo;</div>
    <p>" Lorem Ipsum is simply dummy text of the printing and typesetting industry. Lorem Ipsum has been the industry's standard dummy text ever since the printer took a galley ever since the printer ever since the printer took a galley. "</p>
    <div class="client-name">Client Name</div>
  </div>
</section>

<section class="contact">
  <h2 class="sec-title">Get in Touch With Us</h2>
  <p class="contact-sub">Need a free quote, or have a question? Get in touch!</p>
  <div class="contact-item" style="left:128px">
    <div class="icon"><svg width="34" height="44" viewBox="0 0 34 44"><path d="M17 2C8.7 2 2 8.6 2 16.8 2 28 17 42 17 42s15-14 15-25.2C32 8.6 25.3 2 17 2z" fill="#33e0c3"/><circle cx="17" cy="16" r="6" fill="#fff"/></svg></div>
    <span>1234 BPWC Lorem ipsum text</span>
  </div>
  <div class="contact-item" style="left:440px">
    <div class="icon"><svg width="40" height="40" viewBox="0 0 40 40"><path d="M10 3l7 9-4 5c2 5 6 9 11 11l5-4 9 7-4 7C18 38 2 22 3 7z" fill="#33e0c3"/></svg></div>
    <span>123 - 456 -7890</span>
  </div>
  <div class="contact-item" style="left:752px">
    <div class="icon"><svg width="42" height="30" viewBox="0 0 42 30"><rect x="1" y="1" width="40" height="28" rx="3" fill="#33e0c3"/><polyline points="3,4 21,17 39,4" fill="none" stroke="#fff" stroke-width="2.5"/></svg></div>
    <span>info@bpwc-collective.com</span>
  </div>
  <div class="field" style="left:122px;top:313px;width:318px;height:55px">Name*</div>
  <div class="field" style="left:450px;top:313px;width:303px;height:55px">Email*</div>
  <div class="field" style="left:762px;top:313px;width:311px;height:55px">Phone*</div>
  <div class="field" style="left:122px;top:374px;width:951px;height:100px">Message*</div>
  <a class="btn-outline">Submit</a>
</section>

<footer class="site-footer">
  <div class="brand">
    <div class="brand-name">BPWC</div>
    <div class="brand-tagline">Brightfold Pattern Works Collective</div>
  </div>
  <div class="social"><i class="on"></i><i></i><i></i></div>
  <nav class="footer-nav"><a href="#">Home</a><a href="#">About Us</a><a href="#">Process</a><a href="#">Services</a><a href="#">Expertise</a><a href="#">Contact Us</a></nav>
  <p class="copyright"><b>©BPWC</b> - 2017 . All Rights Reserved.</p>
</footer>

</body>
</html>
```